Corp. Logo & Business Card for KVT Printing Services Ltd.

We have been in business 40 years need a stunding Corp.
Logo that shows great 3D graphics & is bright in colors so
our customers will want us to design their Corp. Logos & do their Printing. just for your information, I like Colors Maroon,
Yellow, Red etc. You do not have to stay with these colors if you have a better color design. The KVT Logo I would like a Very distinctive Font & can be Mulit Color.
I have attached what we are using now, I like the Red Gold with the bright sun light
behind the copy to attach attention.

KVT
Dorwen Services Ltd.
P.O. Box 4630, Brea, CA 92817
714.389.4125 ext. 316
714.389.4190 Fax
wade @ mytradeworkshop-sample.com
www.kvtcardworks-sample.com

KVT
Dorwen Services Ltd.
714.389.4125 ext. 316
714.389.4190 Fax

Dear Designers; You all did a great job.

Thanks

Wade Benfield

```html
<!DOCTYPE html>
<html lang="en">
<head>
<meta charset="utf-8">
<title>KVT Dorwen Services Ltd. — Business Card</title>
<link rel="stylesheet" href="https://fonts.googleapis.com/css2?family=Cormorant+Garamond:ital,wght@0,600;0,700;1,600;1,700&display=swap">
<style>
  :root {
    --ink-black: #0b0b0b;
    --ink-charcoal: #232323;
    --maroon: #6e1416;
    --maroon-dark: #3a0d0e;
    --signal-red: #e0322c;
    --cream: #f7f3b8;
    --cream-shade: #d9d39a;
    --peach: #f5c8a0;
    --rose: #f0a8a0;
  }
  * { margin: 0; padding: 0; box-sizing: border-box; }
  html, body {
    width: 1200px; height: 686px; overflow: hidden;
    background: var(--ink-black);
  }
  .card {
    position: relative; width: 1200px; height: 686px; overflow: hidden;
    font-family: "Cormorant Garamond", Georgia, serif;
    font-variant-numeric: lining-nums;
    font-feature-settings: "lnum" 1;
  }
  .card-background {
    position: absolute; inset: 0;
    background: linear-gradient(135deg, var(--ink-charcoal) 0%, var(--ink-black) 55%, var(--ink-charcoal) 100%);
  }
  .brand-mark {
    position: absolute; left: 40px; top: 72px;
    display: flex; align-items: center; gap: 14px;
  }
  .brand-square {
    width: 44px; height: 44px; background: var(--maroon);
  }
  .brand-name {
    font-size: 64px; font-weight: 700; color: var(--signal-red); line-height: 1;
  }
  .company-name {
    position: absolute; left: 269px; top: 92px;
    font-size: 42px; font-weight: 700; font-style: italic;
    color: var(--signal-red); line-height: 1;
  }
  .tagline {
    position: absolute; right: 25px; top: 174px;
    font-size: 34px; font-weight: 700; font-style: italic;
    color: var(--rose); line-height: 1;
    text-shadow: 1px 1px 0 var(--maroon-dark), 2px 2px 2px #000;
  }
  .name-band {
    position: absolute; left: 0; top: 238px; width: 1200px; height: 107px;
    background: var(--cream);
    border-top: 3px solid var(--maroon);
    border-bottom: 3px solid var(--maroon);
    box-shadow: 0 3px 0 #3d3d2a;
    display: flex; align-items: center; justify-content: center;
  }
  .person-name {
    font-size: 60px; font-weight: 600; font-style: italic;
    color: var(--maroon-dark);
    text-shadow: 2px 2px 2px rgba(120, 60, 60, 0.45);
  }
  .info-box {
    position: absolute;
    background: var(--cream);
    border: 3px solid var(--maroon);
    box-shadow: inset -3px -3px 0 var(--cream-shade), 2px 2px 3px #000;
    color: var(--maroon-dark);
    font-weight: 600;
    text-shadow: 1px 1px 1px rgba(120, 60, 60, 0.4);
  }
  .address-line {
    left: 42px; width: 303px; height: 60px;
    font-size: 32px; padding-left: 46px;
    display: flex; align-items: center;
  }
  .address-line.street { top: 413px; }
  .address-line.city { top: 520px; }
  .contact-line {
    left: 857px; width: 305px;
    display: flex; align-items: flex-start; padding: 8px 12px 0 10px;
  }
  .contact-line.phone { top: 408px; height: 98px; }
  .contact-line.fax { top: 529px; height: 62px; align-items: center; padding-top: 0; }
  .contact-icon { width: 42px; height: 42px; flex: none; margin-top: 8px; }
  .contact-line.fax .contact-icon { margin-top: 0; }
  .contact-text { flex: 1; text-align: right; }
  .contact-number { font-size: 33px; display: block; line-height: 1.25; }
  .contact-ext { font-size: 25px; display: block; line-height: 1.1; }
  .email {
    position: absolute; left: 0; width: 1188px; top: 622px;
    text-align: center;
    font-size: 31px; font-weight: 700; font-style: italic;
    color: var(--peach);
    text-shadow: 1px 1px 0 var(--maroon-dark), 2px 2px 2px #000;
  }
</style>
</head>
<body>
<main class="card">
  <div class="card-background" role="img" aria-label="Dark background with a faint diagonal pattern of the company web address"></div>

  <div class="brand-mark">
    <span class="brand-square"></span>
    <span class="brand-name">KVT</span>
  </div>
  <div class="company-name">Dorwen Services Ltd.</div>
  <div class="tagline">Uniting Print &amp; Promotional Goods Since 1986</div>

  <section class="name-band">
    <h1 class="person-name">Wade Benfield</h1>
  </section>

  <div class="info-box address-line street">P.O. Box 4630</div>
  <div class="info-box address-line city">Brea, CA 92817</div>

  <div class="info-box contact-line phone">
    <svg class="contact-icon" viewBox="0 0 42 42" aria-hidden="true">
      <path d="M9 5 C5 7 4 12 6 18 C9 27 16 34 25 37 C30 39 35 38 37 34 L32 28 C30 27 28 28 26 30 C21 28 15 22 13 17 C15 15 16 13 15 11 Z" fill="#1a1a1a"/>
    </svg>
    <div class="contact-text">
      <span class="contact-number">714.389.4125</span>
      <span class="contact-ext">ext. 316</span>
    </div>
  </div>

  <div class="info-box contact-line fax">
    <svg class="contact-icon" viewBox="0 0 42 42" aria-hidden="true">
      <rect x="12" y="3" width="18" height="16" fill="#fff" stroke="#1a1a1a" stroke-width="2"/>
      <line x1="15" y1="8" x2="27" y2="8" stroke="#1a1a1a" stroke-width="1.5"/>
      <line x1="15" y1="12" x2="27" y2="12" stroke="#1a1a1a" stroke-width="1.5"/>
      <rect x="4" y="19" width="34" height="18" rx="2" fill="#1a1a1a"/>
      <rect x="8" y="23" width="10" height="3" fill="#f7f3b8"/>
      <rect x="24" y="23" width="10" height="8" fill="#555"/>
    </svg>
    <div class="contact-text">
      <span class="contact-number">714.389.4190</span>
    </div>
  </div>

  <div class="email">wade @ mytradeworkshop-sample.com</div>
</main>
</body>
</html>
```